WebSite

Hi,

I need a (responsive?) website for a company that has 3 core businesses:

Hosting
Web design (also logo design)
and ICT systems management

The hosting part has a whois that can be searched, and from there a domain can be registered or moved if it is taken and the move code is known.
Also a pricelist for the 4 different types of packages + add-ons.

The web design part has got to have a small portfolio section.

The ICT management section is just an ordinary page with some info on the work the company does.

And off course a contact page...

http://sh1.vq-serverhuis.nl/cgi-sys/defaultwebpage.cgi

It is a Dutch company, the logo is provided.

I like clean designs, not to busy or to dark, just good look and feel and modern!

I like those single page (with pages that flout into each other etc.) designs (like: http://www.lumaxo.com/trel) but that kind of sites needs to be coded also, that would be part of the job than!

This is my first time here so I do not know if more information is needed or what happens next :)

http://nineweavers.com/#!portfolio-mtolk to give another example of what I like, a site like that is great! 

Hello,

I recieved some designs already but I was hoping for some more creativity, I do not want a design I can buy at Layoutgrotto, I really am in need for something that goes with my logo and looks unique (see last link from brief).

```html
<!DOCTYPE html>
<html lang="en">
<head>
<meta charset="utf-8">
<title>VQ Services</title>
<link rel="stylesheet" href="https://fonts.googleapis.com/css2?family=Open+Sans:wght@400;600;700&family=Gilda+Display&display=swap">
<style>
:root{
  --brand-blue:#1d5a92;
  --navy:#0e3a66;
  --nav-dark:#0b3459;
  --cream:#f5ebda;
  --ink:#3b3b3b;
  --muted:#777;
  --footer:#4a4a4a;
  --footer-line:#3c3c3c;
  --footer-text:#c9c9c9;
  --white:#fff;
}
*{box-sizing:border-box;margin:0;padding:0}
html,body{width:1060px;height:1200px;overflow:hidden;background:var(--white)}
body{position:relative;font-family:"Open Sans",Arial,sans-serif;color:var(--ink)}
.top-strip{position:absolute;left:0;top:0;width:1060px;height:8px;background:var(--brand-blue)}
.site-header{position:absolute;left:0;top:8px;width:1060px;height:108px;background:var(--cream)}
.brand{position:absolute;left:128px;top:40px;display:flex;align-items:center;gap:10px;font-size:24px;font-weight:700;color:var(--brand-blue)}
.brand-dot{width:24px;height:24px;border-radius:50%;background:var(--brand-blue)}
.contact-info{position:absolute;right:125px;top:29px;text-align:right}
.contact-call{font-size:15px;color:#222;letter-spacing:.5px}
.contact-mail{font-size:11px;font-weight:600;color:var(--brand-blue);margin-top:9px}
.hero{position:absolute;left:0;top:116px;width:1060px;height:432px;
  background:radial-gradient(ellipse at 50% 40%,#e2e6ef 0%,#b5bdd3 45%,#4a5b86 78%,#1f2c4d 100%)}
.nav-band{position:absolute;left:0;top:116px;width:1060px;height:6px;background:var(--nav-dark)}
.main-nav{position:absolute;left:0;top:116px;width:1060px;height:44px}
.main-nav svg{position:absolute;left:0;top:0}
.main-nav ul{position:absolute;left:0;top:13px;width:1060px;list-style:none}
.main-nav li{position:absolute;transform:translateX(-50%);font-size:14px;color:var(--white);white-space:nowrap}
.slider-dots{position:absolute;top:512px;left:518px;display:flex;gap:8px}
.slider-dots span{width:11px;height:11px;border-radius:50%;background:#4a4d55}
.slider-dots span.active{background:var(--brand-blue)}
.section-title{position:absolute;left:0;width:1060px;text-align:center;font-family:"Gilda Display",Georgia,serif;font-weight:400;font-size:25px;color:var(--brand-blue)}
.welcome-title{top:572px}
.welcome-text{position:absolute;left:125px;top:611px;width:810px;text-align:center;font-size:11px;line-height:20px;color:#333}
.services-title{top:684px}
.service-card{position:absolute;top:728px;width:242px;height:208px;border:1px solid #ddd;background:var(--white);box-shadow:0 1px 3px rgba(0,0,0,.08)}
.service-image{position:absolute;left:12px;top:12px;width:218px;height:95px}
.img-hosting{background:linear-gradient(180deg,#cfd3d6 0%,#6f7a72 50%,#1f3326 100%)}
.img-web{background:radial-gradient(circle at 65% 55%,#4c86c4 0%,#1a2f5a 40%,#0a0f22 100%)}
.img-ict{background:linear-gradient(120deg,#3e5f76 0%,#8fb2c4 55%,#203847 100%)}
.service-name{position:absolute;left:12px;top:114px;font-family:"Gilda Display",Georgia,serif;font-weight:400;font-size:19px;color:var(--brand-blue);white-space:nowrap}
.service-text{position:absolute;left:13px;top:141px;width:222px;font-size:10px;line-height:17px;color:var(--muted)}
.learn-more{position:absolute;left:14px;top:183px;font-size:11px;font-weight:700;color:var(--navy)}
.learn-more b{color:#8a97a8}
.site-footer{position:absolute;left:0;top:973px;width:1060px;height:227px;background:var(--footer)}
.footer-col{position:absolute;top:18px}
.footer-col h4{font-size:11px;font-weight:400;color:#eee;margin-bottom:14px}
.footer-col li{list-style:none;font-size:10px;color:var(--footer-text);line-height:20px}
.social li{display:flex;align-items:center;gap:12px;line-height:25px}
.social i{width:20px;height:20px;border-radius:50%}
.newsletter-input{position:absolute;left:698px;top:46px;width:237px;height:28px;background:#8f8f8f}
.signup{position:absolute;left:871px;top:88px;width:64px;height:29px;background:#f4f4f4;border:1px solid #ccc;font-size:10px;color:#999;text-align:center;line-height:27px}
.badge{position:absolute;left:704px;top:89px;width:58px;height:58px;border-radius:50%;background:radial-gradient(circle,#c9a641 0%,#8a6c1f 70%,#5c4713 100%)}
.footer-rule{position:absolute;left:0;top:165px;width:1060px;height:1px;background:var(--footer-line)}
.copyright{position:absolute;left:125px;top:188px;font-size:10px;color:#eee}
</style>
</head>
<body>
<div class="top-strip"></div>
<header class="site-header">
  <div class="brand"><span class="brand-dot"></span>VQ Services</div>
  <div class="contact-info">
    <p class="contact-call">CALL : (020) 555-0147</p>
    <p class="contact-mail">E-mail: info@VQServices.org</p>
  </div>
</header>

<div class="hero" role="img" aria-label="Photo of a businessman in a suit touching a glowing cloud icon"></div>

<div class="nav-band"></div>
<nav class="main-nav">
  <svg width="1060" height="44" viewBox="0 0 1060 44">
    <path d="M118 4 Q132 4 136 20 Q141 39 158 40 L902 40 Q919 39 924 20 Q928 4 942 4 Z" fill="#0d3a64"/>
  </svg>
  <ul>
    <li style="left:167px">Home</li>
    <li style="left:280px">About us</li>
    <li style="left:400px">Services</li>
    <li style="left:514px">Gallery</li>
    <li style="left:616px">Blog</li>
    <li style="left:736px">Testimonials</li>
    <li style="left:876px">Contact us</li>
  </ul>
</nav>
<div class="slider-dots"><span class="active"></span><span></span><span></span></div>

<h1 class="section-title welcome-title">Welcome To Our Company</h1>
<p class="welcome-text">There are many variations of passages of Lorem Ipsum available, but the majority have suffered alteration in some form, by injected humour, or randomised words which don't look even slightly believable. If you are going to use a passage of Lorem Ipsum, you need to be sure there isn't anything embarrassingeven slightly believable.&nbsp; Ipsum, you&nbsp; hidden in the middle of text.</p>

<h2 class="section-title services-title">Our Services</h2>

<article class="service-card" style="left:125px">
  <div class="service-image img-hosting" role="img" aria-label="Photo of a server room with racks"></div>
  <h3 class="service-name">Hosting</h3>
  <p class="service-text">Lorem Ipsum available, but the majority have suffered alteration in some form</p>
  <span class="learn-more">Learn More <b>›</b></span>
</article>
<article class="service-card" style="left:409px">
  <div class="service-image img-web" role="img" aria-label="Photo of a digital globe held in a hand"></div>
  <h3 class="service-name">Web &amp; Logo design</h3>
  <p class="service-text">Lorem Ipsum available, but the majority have suffered alteration in some form</p>
  <span class="learn-more">Learn More <b>›</b></span>
</article>
<article class="service-card" style="left:693px">
  <div class="service-image img-ict" role="img" aria-label="Illustration of circuit lines and binary code"></div>
  <h3 class="service-name">ICT systems management</h3>
  <p class="service-text">Lorem Ipsum available, but the majority have suffered alteration in some form</p>
  <span class="learn-more">Learn More <b>›</b></span>
</article>

<footer class="site-footer">
  <div class="footer-col" style="left:125px"><h4>INFORMATION</h4><ul><li>About Us</li><li>Privacy Policy</li><li>Site Map</li><li>Search Terms</li><li>Advanced Search</li></ul></div>
  <div class="footer-col" style="left:263px"><h4>WHY BUY FROM US</h4><ul><li>Customer Service</li><li>Shipping &amp; Returns</li><li>Secure Shopping</li><li>International Shipping</li><li>Affiliates</li></ul></div>
  <div class="footer-col" style="left:422px"><h4>MY ACCOUNT</h4><ul><li>My Cart</li><li>My Wishlist</li><li>Checkout</li><li>Track My order</li><li>Help</li></ul></div>
  <div class="footer-col social" style="left:563px"><h4>FOLLOW US</h4><ul>
    <li><i style="background:#3b5a9a"></i>Friendbook</li>
    <li><i style="background:#2aa3df"></i>Chirper</li>
    <li><i style="background:#d8322a"></i>Tubecast</li>
    <li><i style="background:#e2463a"></i>Circles Plus</li>
  </ul></div>
  <div class="footer-col" style="left:700px"><h4>NEWSLETTER SIGNUP</h4></div>
  <div class="newsletter-input"></div>
  <div class="signup">SIGNUP</div>
  <div class="badge"></div>
  <div class="footer-rule"></div>
  <p class="copyright">Copyright © 2014 Company Name.&nbsp; All right reserved.</p>
</footer>
</body>
</html>
```